The Meadow Fellowship Pitchdeck Template

The Meadow Fellowship would like a branded pitch deck template design for members to use when presenting their projects and proposals. The deck should include 10-15 different slide designs, each with the same branded theme, but with a variety of icon graphics and other design features that will empower members to easily create a beautiful pitch deck just by adding written content.

Please visit themeadow.org to get a sense for our branding - purple, space, galaxy, white font and the planetary logo are some commonalities.

Here are 2 google drive links with some additional designs

https://files.brindlecove.net/share/u/1/folders/7QxPanLr02TbKvemZcW-J4hd9Ryyu3Mk

https://files.brindlecove.net/share/u/1/folders/4Hn2k-Ts8V91-rYDbq651yemvhpA_kr3

```html
<!DOCTYPE html>
<html lang="en">
<head>
<meta charset="utf-8">
<title>The Meadow Fellowship – Pitch Deck Template</title>
<link rel="stylesheet" href="https://fonts.googleapis.com/css2?family=Montserrat:wght@400;500;600;700;800&display=swap">
<style>
:root{
  --page:#b9b9bb;
  --night:#0d0f26;
  --night-2:#1a1640;
  --violet:#5a2f86;
  --violet-soft:#3d2a6e;
  --plum:#7b2f8f;
  --magenta:#c2338f;
  --pink:#e0336f;
  --blue:#2d78d8;
  --white:#ffffff;
  --muted:#d9d4ea;
  --line:rgba(255,255,255,.35);
}
*{box-sizing:border-box;margin:0;padding:0}
html,body{width:1200px;height:2417px;overflow:hidden;background:var(--page)}
body{position:relative;font-family:"Montserrat",Arial,sans-serif;color:var(--white)}
.slide{position:absolute;width:553px;height:311px;overflow:hidden;
  background:radial-gradient(ellipse at 70% 30%,#2b2560 0%,var(--night) 65%)}
.col-a{left:33px}.col-b{left:616px}
.photo{position:absolute}
.abs{position:absolute}
.brand{position:absolute;right:22px;top:30px;font-size:8px;font-weight:700;letter-spacing:.5px;display:flex;align-items:center;gap:5px}
.brand::before{content:"";width:9px;height:9px;border-radius:50%;background:var(--white)}
.h{position:absolute;font-weight:700;font-size:15px;letter-spacing:.2px;text-transform:uppercase}
.body{position:absolute;font-size:7px;line-height:1.5;color:var(--muted)}
.ctitle{font-weight:700;font-size:9.5px;text-align:center}
.ctext{font-size:6.6px;line-height:1.55;text-align:center;color:var(--muted)}
.card{position:absolute;width:120px;text-align:center}
</style>
</head>
<body>

<!-- Cover -->
<section class="slide col-a" style="top:32px;background:radial-gradient(ellipse at 50% 20%,#6b57a8 0%,#3b2a72 45%,#1b1440 100%)" role="img" aria-label="Cover slide: figure standing on a rock under a purple nebula sky">
  <div class="photo" style="left:210px;top:170px;width:130px;height:141px;background:radial-gradient(ellipse at 50% 100%,#120c2a 20%,transparent 70%)"></div>
  <div class="abs" style="top:82px;width:100%;text-align:center;font-size:9px;font-weight:700;letter-spacing:.6px">The Meadow Fellowship</div>
  <div class="abs" style="top:138px;width:100%;text-align:center;font-size:23px;font-weight:700;letter-spacing:.3px">PRESENTATION TITLE HERE</div>
  <div class="abs" style="top:164px;width:100%;text-align:center;font-size:6.5px;letter-spacing:14px">SUBTITLE GOES HERE</div>
</section>

<!-- Table of content -->
<section class="slide col-b" style="top:32px;background:linear-gradient(180deg,#b2477a 0%,#7c3262 50%,#3a1e3e 100%)">
  <div class="photo" role="img" aria-label="Glowing pink planet rings over a desert landscape" style="left:0;top:0;width:278px;height:311px;background:radial-gradient(ellipse at 70% 25%,#f17db0 0%,#b2477a 40%,#5b2547 100%)"></div>
  <div class="abs" style="left:278px;top:0;width:275px;height:311px;background:rgba(70,25,70,.55)"></div>
  <div class="brand">The Meadow Fellowship</div>
  <div class="h" style="left:362px;top:66px;font-size:14px">Table of Content</div>
  <div class="abs" style="left:346px;top:100px;width:180px;font-size:8px">
    <div style="display:grid;grid-template-rows:repeat(9,20.6px)">
      <div style="display:flex;align-items:center;gap:10px;border-bottom:1px solid var(--line)"><span style="width:10px;height:10px;border-radius:50%;background:var(--plum);font-size:5px;display:flex;align-items:center;justify-content:center">1</span>Introduction</div>
      <div style="display:flex;align-items:center;gap:10px;border-bottom:1px solid var(--line)"><span style="width:10px;height:10px;border-radius:50%;background:var(--plum);font-size:5px;display:flex;align-items:center;justify-content:center">2</span>About Us</div>
      <div style="display:flex;align-items:center;gap:10px;border-bottom:1px solid var(--line)"><span style="width:10px;height:10px;border-radius:50%;background:var(--plum);font-size:5px;display:flex;align-items:center;justify-content:center">3</span>Welcome Message</div>
      <div style="display:flex;align-items:center;gap:10px;border-bottom:1px solid var(--line)"><span style="width:10px;height:10px;border-radius:50%;background:var(--plum);font-size:5px;display:flex;align-items:center;justify-content:center">4</span>Our Services</div>
      <div style="display:flex;align-items:center;gap:10px;border-bottom:1px solid var(--line)"><span style="width:10px;height:10px;border-radius:50%;background:var(--plum);font-size:5px;display:flex;align-items:center;justify-content:center">5</span>Our Team</div>
      <div style="display:flex;align-items:center;gap:10px;border-bottom:1px solid var(--line)"><span style="width:10px;height:10px;border-radius:50%;background:var(--plum);font-size:5px;display:flex;align-items:center;justify-content:center">6</span>Infographic</div>
      <div style="display:flex;align-items:center;gap:10px;border-bottom:1px solid var(--line)"><span style="width:10px;height:10px;border-radius:50%;background:var(--plum);font-size:5px;display:flex;align-items:center;justify-content:center">7</span>Chart</div>
      <div style="display:flex;align-items:center;gap:10px;border-bottom:1px solid var(--line)"><span style="width:10px;height:10px;border-radius:50%;background:var(--plum);font-size:5px;display:flex;align-items:center;justify-content:center">8</span>Table</div>
      <div style="display:flex;align-items:center;gap:10px;border-bottom:1px solid var(--line)"><span style="width:10px;height:10px;border-radius:50%;background:var(--plum);font-size:5px;display:flex;align-items:center;justify-content:center">9</span>Contact Us</div>
    </div>
  </div>
</section>

<!-- Introduction -->
<section class="slide col-a" style="top:372px;background:radial-gradient(ellipse at 40% 30%,#3d3068 0%,#231b45 55%,#140f2c 100%)">
  <div class="abs" style="left:40px;top:34px;font-size:8px;font-weight:700;display:flex;align-items:center;gap:5px"><span style="width:9px;height:9px;border-radius:50%;background:#fff"></span>The Meadow Fellowship</div>
  <div class="h" style="left:40px;top:104px">Introduction</div>
  <p class="body" style="left:40px;top:138px;width:220px;text-align:justify">Lorem ipsum dolor sit amet, consectetuer adipiscing elit, sed diam nonummy nibh euismod tincidunt ut laoreet dolore magna aliquam erat volutpat. Ut wisi enim ad minim veniam, quis nostrud exerci tation ullamcorper suscipit lobortis nisl ut aliquip ex ea commodo consequat. Duis autem vel eum iriure dolor in hendrerit in vulputate velit esse molestie consequat, vel illum dolore eu feugiat nulla facilisis</p>
  <div class="photo" role="img" aria-label="Close-up of an eye with an astronaut reflected in the iris" style="left:337px;top:42px;width:178px;height:226px;background:radial-gradient(circle at 50% 50%,#8fa9c4 0%,#4c5f7a 25%,#a2603c 55%,#d49a6e 100%)"></div>
</section>

<!-- Three content cards -->
<section class="slide col-b" style="top:372px">
  <div class="h" style="left:41px;top:30px">Your Title Here</div>
  <div class="brand">The Meadow Fellowship</div>
  <div class="photo" role="img" aria-label="Fiery orange planet surface" style="left:94px;top:83px;width:91px;height:91px;background:radial-gradient(circle at 40% 40%,#f3b45a 0%,#a4521d 45%,#2a160f 100%)"></div>
  <div class="photo" role="img" aria-label="Purple galaxy above desert dunes" style="left:239px;top:83px;width:91px;height:91px;background:radial-gradient(circle at 50% 35%,#c07ad8 0%,#5a3294 50%,#1b1a3a 100%)"></div>
  <div class="photo" role="img" aria-label="Pink glowing galaxy streak in space" style="left:384px;top:83px;width:91px;height:91px;background:radial-gradient(circle at 50% 50%,#e26ab8 0%,#4a2163 45%,#0f0d24 100%)"></div>
  <div class="card" style="left:80px;top:186px"><div class="ctitle">Content Title</div><p class="ctext" style="margin-top:4px">Lorem ipsum dolor sit amet, consectetuer adipiscing e lit, sed diam nonummy nibh euismod tincidunt ut laoreet dolore magna aliquam erat</p></div>
  <div class="card" style="left:225px;top:186px"><div class="ctitle">Content Title</div><p class="ctext" style="margin-top:4px">Lorem ipsum dolor sit amet, consectetuer adipiscing e lit, sed diam nonummy nibh euismod tincidunt ut laoreet dolore magna aliquam erat</p></div>
  <div class="card" style="left:370px;top:186px"><div class="ctitle">Content Title</div><p class="ctext" style="margin-top:4px">Lorem ipsum dolor sit amet, consectetuer adipiscing e lit, sed diam nonummy nibh euismod tincidunt ut laoreet dolore magna aliquam erat</p></div>
</section>

<!-- Three tall images -->
<section class="slide col-a" style="top:713px;background:radial-gradient(ellipse at 70% 60%,#3a1f4a 0%,#1a1432 55%,#0d0c20 100%)">
  <div class="brand">The Meadow Fellowship</div>
  <div class="photo" role="img" aria-label="Misty mountain cliffs with a portal" style="left:39px;top:101px;width:69px;height:157px;background:linear-gradient(180deg,#d7dce3 0%,#7e8796 50%,#2a2c38 100%)"></div>
  <div class="photo" role="img" aria-label="Hand holding a glowing crystal" style="left:115px;top:51px;width:69px;height:159px;background:linear-gradient(180deg,#2d6a7a 0%,#163a52 50%,#0f1a2a 100%)"></div>
  <div class="photo" role="img" aria-label="Colourful nebula over a floating island" style="left:192px;top:101px;width:69px;height:157px;background:radial-gradient(circle at 50% 35%,#d85aa6 0%,#5a3aa0 45%,#16142e 100%)"></div>
  <div class="abs" style="left:62px;top:240px;font-size:7px;font-weight:700">Title 1</div>
  <div class="abs" style="left:138px;top:191px;font-size:7px;font-weight:700">Title 2</div>
  <div class="abs" style="left:218px;top:242px;font-size:7px;font-weight:700">Title 3</div>
  <div class="h" style="left:314px;top:108px">Your Title Here</div>
  <p class="body" style="left:314px;top:142px;width:185px">Lorem ipsum dolor sit amet, consectetuer adipiscing elit, sed diam nonummy nibh euismod tincidunt ut laoreet dolore magna aliquam erat volutpat. Ut wisi enim ad minim veniam, quis nostrud exerci tation ullamcorper suscipit lobortis</p>
</section>

<!-- Circles on white -->
<section class="slide col-b" style="top:713px;background:var(--white)">
  <div class="photo" role="img" aria-label="Dark purple rocky terrain" style="left:0;top:0;width:553px;height:161px;background:linear-gradient(180deg,#3a3f58 0%,#2c2a52 30%,#352c62 100%)"></div>
  <div class="h" style="left:32px;top:36px">Your Title Here</div>
  <div class="brand">The Meadow Fellowship</div>
  <p class="body" style="left:32px;top:62px;width:390px;color:var(--white)">Lorem ipsum dolor sit amet, consectetuer adipiscing elit, sed diam nonummy nibh euismod tincidunt ut laoreet dolore magna aliquam erat volutpat. Ut wisi enim ad minim veniam, quis nostrud exerci tation ullamcorper suscipit lobortis nisl ut aliquip ex ea commodo consequat. Duis autem vel eum iriure dolor in</p>
  <div class="photo" role="img" aria-label="Purple particle sphere" style="left:95px;top:116px;width:88px;height:88px;border-radius:50%;border:3px solid #fff;background:radial-gradient(circle,#9b5be0 0%,#4a2aa0 55%,#1d1550 100%)"></div>
  <div class="photo" role="img" aria-label="Dark night sky with light trails" style="left:241px;top:116px;width:88px;height:88px;border-radius:50%;border:3px solid #fff;background:radial-gradient(circle at 50% 70%,#6a6a4a 0%,#2a2e3e 50%,#12151f 100%)"></div>
  <div class="photo" role="img" aria-label="Pale blue sky over Earth's horizon" style="left:385px;top:116px;width:88px;height:88px;border-radius:50%;border:3px solid #fff;background:radial-gradient(circle at 50% 30%,#cfdbe6 0%,#7d9bb8 50%,#2a4a78 100%)"></div>
  <div class="card" style="left:79px;top:216px;color:#111"><div class="ctitle">Content Title</div><p class="ctext" style="color:#333;margin-top:3px">Lorem ipsum dolor sit<br>amet, consectetuer</p></div>
  <div class="card" style="left:225px;top:216px;color:#111"><div class="ctitle">Content Title</div><p class="ctext" style="color:#333;margin-top:3px">Lorem ipsum dolor sit<br>amet, consectetuer</p></div>
  <div class="card" style="left:369px;top:216px;color:#111"><div class="ctitle">Content Title</div><p class="ctext" style="color:#333;margin-top:3px">Lorem ipsum dolor sit<br>amet, consectetuer</p></div>
</section>

<!-- Section divider -->
<section class="slide col-a" style="top:1053px;background:linear-gradient(135deg,#2f2a45 0%,#3c3658 45%,#2a2440 100%)" role="img" aria-label="Rocky mountains with a swirling portal and a lone figure">
  <div class="abs" style="left:40px;top:176px;font-size:32px;font-weight:800">01</div>
  <div class="h" style="left:40px;top:223px">Section Title Here</div>
  <p class="body" style="left:40px;top:247px;width:230px;color:var(--white)">Lorem ipsum dolor sit amet, consectetuer adipiscing elit, sed diam nonummy nibh euismod tincidunt ut laoreet dolore</p>
</section>

<!-- Timeline -->
<section class="slide col-b" style="top:1053px;background:radial-gradient(ellipse at 70% 90%,#5a3a8a 0%,#272258 45%,#12112e 100%)">
  <div class="h" style="left:32px;top:40px">Timeline</div>
  <div class="brand">The Meadow Fellowship</div>
  <svg class="abs" style="left:0;top:0" width="553" height="311">
    <line x1="80" y1="156" x2="470" y2="156" stroke="#9fb0ff" stroke-width="1"/>
    <g fill="#fff"><circle cx="91" cy="156" r="4"/><circle cx="180" cy="156" r="4"/><circle cx="270" cy="156" r="4"/><circle cx="359" cy="156" r="4"/><circle cx="449" cy="156" r="4"/></g>
    <g fill="rgba(150,180,255,.35)"><circle cx="91" cy="156" r="9"/><circle cx="180" cy="156" r="9"/><circle cx="270" cy="156" r="9"/><circle cx="359" cy="156" r="9"/><circle cx="449" cy="156" r="9"/></g>
  </svg>
  <div class="card" style="left:31px;top:118px;width:120px"><div style="font-weight:700;font-size:11px">20YY</div><p class="ctext" style="margin-top:48px">Lorem ipsum<br>dolor sit amet,<br>consectetuer<br>adipiscing e lit,<br>sed diam</p></div>
  <div class="card" style="left:120px;top:118px;width:120px"><div style="font-weight:700;font-size:11px">20YY</div><p class="ctext" style="margin-top:48px">Lorem ipsum<br>dolor sit amet,<br>consectetuer<br>adipiscing e lit,<br>sed diam</p></div>
  <div class="card" style="left:210px;top:118px;width:120px"><div style="font-weight:700;font-size:11px">20YY</div><p class="ctext" style="margin-top:48px">Lorem ipsum<br>dolor sit amet,<br>consectetuer<br>adipiscing e lit,<br>sed diam</p></div>
  <div class="card" style="left:299px;top:118px;width:120px"><div style="font-weight:700;font-size:11px">20YY</div><p class="ctext" style="margin-top:48px">Lorem ipsum<br>dolor sit amet,<br>consectetuer<br>adipiscing e lit,<br>sed diam</p></div>
  <div class="card" style="left:389px;top:118px;width:120px"><div style="font-weight:700;font-size:11px">20YY</div><p class="ctext" style="margin-top:48px">Lorem ipsum<br>dolor sit amet,<br>consectetuer<br>adipiscing e lit,<br>sed diam</p></div>
</section>

<!-- Chart -->
<section class="slide col-a" style="top:1393px;background:radial-gradient(ellipse at 40% 85%,#4a3a6e 0%,#221c44 45%,#12102a 100%)">
  <div class="brand">The Meadow Fellowship</div>
  <div class="h" style="left:40px;top:91px">Chart Slide</div>
  <p class="body" style="left:40px;top:130px;width:166px">Lorem ipsum dolor sit amet, consectetuer adipiscing elit, sed diam nonummy nibh euismod tincidunt ut laoreet dolore magna aliquam erat volutpat. Ut wisi enim ad minim veniam, quis nostrud exerci tation ullamcorper suscipit lobortis nisl ut aliquip ex ea commodo consequat. Duis autem vel eum iriure dolor in hendrerit in vulputate velit esse molestie consequat, vel illum dolore eu feugiat nulla facilisis at vero eros et</p>
  <svg class="abs" style="left:0;top:0" width="553" height="311" font-family="Montserrat, sans-serif" font-size="6.5" font-weight="700" fill="#fff" text-anchor="middle">
    <defs><linearGradient id="bar" x1="0" y1="0" x2="0" y2="1"><stop offset="0" stop-color="#a43cb8"/><stop offset="1" stop-color="#6a2a8e"/></linearGradient></defs>
    <g fill="#1a1630"><rect x="265" y="95" width="31" height="151"/><rect x="309" y="95" width="31" height="151"/><rect x="353" y="95" width="31" height="151"/><rect x="397" y="95" width="31" height="151"/><rect x="441" y="95" width="31" height="151"/><rect x="485" y="95" width="31" height="151"/></g>
    <g fill="url(#bar)"><rect x="265" y="216" width="31" height="30"/><rect x="309" y="201" width="31" height="45"/><rect x="353" y="178" width="31" height="68"/><rect x="397" y="170" width="31" height="76"/><rect x="441" y="155" width="31" height="91"/><rect x="485" y="125" width="31" height="121"/></g>
    <text x="280" y="240">20%</text><text x="324" y="240">30%</text><text x="368" y="240">45%</text><text x="412" y="240">50%</text><text x="456" y="240">60%</text><text x="500" y="240">80%</text>
  </svg>
</section>

<!-- Table -->
<section class="slide col-b" style="top:1393px">
  <div class="h" style="left:32px;top:40px">Table Slide</div>
  <div class="brand">The Meadow Fellowship</div>
  <div class="abs" style="left:92px;top:91px;width:394px;height:190px;border-radius:8px;background:rgba(70,72,110,.45);font-size:6.8px">
    <svg class="abs" style="left:14px;top:8px" width="40" height="6"><circle cx="3" cy="3" r="2" fill="#3aa0ff"/><circle cx="11" cy="3" r="2" fill="#f0a33a"/><circle cx="19" cy="3" r="2" fill="#e0336f"/></svg>
    <div class="abs" style="left:17px;top:22px;font-weight:700">Lorem ipsum dolor sit amet, consectetuer adipiscing elit, sed diam</div>
    <div class="abs" style="left:0;top:49px;width:394px;height:18px;background:rgba(90,94,140,.55)"></div>
    <div class="abs" style="left:17px;top:54px;font-weight:700">Lorem ipsum</div>
    <div class="abs" style="left:95px;top:54px;font-weight:700">Lorem ipsum</div>
    <div class="abs" style="left:290px;top:54px;font-weight:700">Lorem</div>
    <div class="abs" style="left:344px;top:54px;font-weight:700">Lorem</div>
    <div class="abs" style="left:17px;top:74px;width:360px;display:grid;grid-template-columns:78px 195px 54px 1fr;row-gap:0">
      <span style="height:24px;border-bottom:1px solid var(--line)">Lorem ipsum</span><span style="border-bottom:1px solid var(--line)">Lorem ipsum dolor sit amet, consectetuer</span><span style="border-bottom:1px solid var(--line)">123</span><span style="color:#3aa0ff;border-bottom:1px solid var(--line)">123</span>
      <span style="height:24px;padding-top:5px;border-bottom:1px solid var(--line)">Lorem ipsum</span><span style="padding-top:5px;border-bottom:1px solid var(--line)">Lorem ipsum dolor sit amet, consectetuer</span><span style="padding-top:5px;border-bottom:1px solid var(--line)">123</span><span style="padding-top:5px;color:#3aa0ff;border-bottom:1px solid var(--line)">123</span>
      <span style="height:24px;padding-top:5px;border-bottom:1px solid var(--line)">Lorem ipsum</span><span style="padding-top:5px;border-bottom:1px solid var(--line)">Lorem ipsum dolor sit amet, consectetuer</span><span style="padding-top:5px;border-bottom:1px solid var(--line)">123</span><span style="padding-top:5px;color:#3aa0ff;border-bottom:1px solid var(--line)">123</span>
      <span style="height:24px;padding-top:5px;border-bottom:1px solid var(--line)">Lorem ipsum</span><span style="padding-top:5px;border-bottom:1px solid var(--line)">Lorem ipsum dolor sit amet, consectetuer</span><span style="padding-top:5px;border-bottom:1px solid var(--line)">123</span><span style="padding-top:5px;color:#3aa0ff;border-bottom:1px solid var(--line)">123</span>
      <span style="height:24px;padding-top:5px">Lorem ipsum</span><span style="padding-top:5px">Lorem ipsum dolor sit amet, consectetuer</span><span style="padding-top:5px">123</span><span style="padding-top:5px;color:#3aa0ff">123</span>
    </div>
  </div>
</section>

<!-- Hexagon infographic -->
<section class="slide col-a" style="top:1733px;background:radial-gradient(ellipse at 65% 40%,#4a3a78 0%,#1f1a42 50%,#100f26 100%)">
  <div class="h" style="left:40px;top:41px">Infographic</div>
  <div class="brand">The Meadow Fellowship</div>
  <svg class="abs" style="left:0;top:0" width="553" height="311" font-family="Montserrat, sans-serif" fill="#fff" text-anchor="middle">
    <polygon points="271,44 318,67 318,113 271,136 224,113 224,67" fill="#7b2f8f"/>
    <polygon points="212,159 259,182 259,228 212,251 165,228 165,182" fill="#2d78d8" stroke="#1c3f7a" stroke-width="4"/>
    <polygon points="332,159 379,182 379,228 332,251 285,228 285,182" fill="#e0336f" stroke="#8a1d52" stroke-width="4"/>
    <g font-size="7" font-weight="700"><text x="271" y="86">Lorem</text><text x="212" y="200">Lorem</text><text x="332" y="200">Lorem</text></g>
    <g font-size="6"><text x="271" y="100">Lorem ipsum dolor sit</text><text x="271" y="110">amet, consectetuer</text><text x="271" y="120">adipiscing elit, sed diam</text>
    <text x="212" y="214">Lorem ipsum dolor sit</text><text x="212" y="224">amet, consectetuer</text><text x="212" y="234">adipiscing elit, sed diam</text>
    <text x="332" y="214">Lorem ipsum dolor sit</text><text x="332" y="224">amet, consectetuer</text><text x="332" y="234">adipiscing elit, sed diam</text></g>
    <g fill="none" stroke="#fff" stroke-width="1"><circle cx="271" cy="72" r="5"/><path d="M207 176v10M207 176h8v4h-8"/><circle cx="332" cy="181" r="5"/></g>
  </svg>
</section>

<!-- Orbit infographic -->
<section class="slide col-b" style="top:1733px;background:radial-gradient(ellipse at 50% 50%,#3b2c70 0%,#1f1a48 50%,#0f0e26 100%)">
  <div class="h" style="left:0;top:41px;width:553px;text-align:center">Infographic</div>
  <div class="brand">The Meadow Fellowship</div>
  <svg class="abs" style="left:0;top:0" width="553" height="311" font-family="Montserrat, sans-serif" fill="#fff">
    <ellipse cx="277" cy="155" rx="140" ry="45" fill="none" stroke="#c9c6e6" stroke-width="1"/>
    <circle cx="277" cy="153" r="62" fill="#5a2f86" opacity=".55"/>
    <circle cx="277" cy="153" r="56" fill="#8a2f9e"/>
    <circle cx="172" cy="121" r="19" fill="#e0336f" stroke="#3a1a4a" stroke-width="4"/>
    <circle cx="189" cy="194" r="19" fill="#c8684a" stroke="#3a1a4a" stroke-width="4"/>
    <circle cx="382" cy="121" r="19" fill="#2d78d8" stroke="#3a1a4a" stroke-width="4"/>
    <circle cx="363" cy="194" r="19" fill="#3bc46a" stroke="#3a1a4a" stroke-width="4"/>
    <g fill="none" stroke="#fff" stroke-width="1.2"><path d="M271 128h12v10h-12zM274 138v6M280 138v6"/><circle cx="172" cy="121" r="6"/><path d="M183 200l12-12M186 200l9-9"/><path d="M374 121h16M382 114v14"/><path d="M356 194h14M363 188v12"/></g>
    <g text-anchor="middle"><text x="277" y="159" font-size="8" font-weight="700">Lorem ipsum</text>
    <g font-size="6"><text x="277" y="171">Lorem ipsum dolor sit amet,</text><text x="277" y="181">consectetuer adipiscing elit,</text><text x="277" y="191">sed diam nonummy nibh</text></g></g>
    <g font-size="6" text-anchor="end"><text x="122" y="113" font-size="7.5" font-weight="700">Lorem ipsum</text><text x="122" y="125">Lorem ipsum dolor sit amet,</text><text x="122" y="135">consectetuer adipiscing elit.</text>
    <text x="152" y="192" font-size="7.5" font-weight="700">Lorem ipsum</text><text x="152" y="204">Lorem ipsum dolor sit amet,</text><text x="152" y="214">consectetuer adipiscing elit.</text></g>
    <g font-size="6"><text x="425" y="113" font-size="7.5" font-weight="700">Lorem ipsum</text><text x="425" y="125">Lorem ipsum dolor sit amet,</text><text x="425" y="135">consectetuer adipiscing elit.</text>
    <text x="400" y="192" font-size="7.5" font-weight="700">Lorem ipsum</text><text x="400" y="204">Lorem ipsum dolor sit amet,</text><text x="400" y="214">consectetuer adipiscing elit.</text></g>
  </svg>
</section>

<!-- Free icons -->
<section class="slide col-a" style="top:2074px;background:radial-gradient(ellipse at 45% 55%,#4a3a80 0%,#231d52 45%,#0f0e28 100%)">
  <div class="h" style="left:0;top:32px;width:553px;text-align:center">Free Icons</div>
  <svg class="abs" style="left:0;top:0" width="553" height="311" fill="none" stroke="#fff" stroke-width="1.3">
    <defs>
      <g id="i-planet"><circle r="10"/><ellipse rx="17" ry="5"/></g>
      <g id="i-flag"><path d="M-4 14V-12h12l-3 5 3 5H-4"/><circle cx="-8" cy="0" r="2"/></g>
      <g id="i-rocket"><path d="M-8 8L6-6l6-6-6 6M-8 8l-4 4M-2-8l10 10"/><rect x="-6" y="-4" width="10" height="8" transform="rotate(-45)"/></g>
      <g id="i-ufo"><ellipse rx="14" ry="5"/><path d="M-8-2a8 8 0 0 1 16 0"/><path d="M-6 6l-3 8M6 6l3 8"/></g>
      <g id="i-robot"><rect x="-8" y="-8" width="16" height="12"/><circle cx="-3" cy="-2" r="1.5"/><circle cx="3" cy="-2" r="1.5"/><path d="M0-8v-5M-10 8h20v6h-20z"/></g>
      <g id="i-helmet"><circle r="12"/><rect x="-8" y="-4" width="16" height="8" rx="3"/></g>
      <g id="i-sun"><circle r="8"/><path d="M0-14v4M0 10v4M-14 0h4M10 0h4M-10-10l3 3M7 7l3 3M-10 10l3-3M7-7l3-3"/></g>
      <g id="i-sat"><rect x="-4" y="-4" width="8" height="8"/><path d="M-16-2h10v4h-10zM6-2h10v4H6zM0 4v8M-6 14h12"/></g>
      <g id="i-scope"><path d="M-12 4l20-10 3 6-20 10zM-2 8l-6 8M-2 8l6 8"/></g>
      <g id="i-ring"><circle r="12"/><circle r="8"/><circle r="4"/></g>
      <g id="i-comet"><circle cx="6" cy="6" r="5"/><path d="M2 2l-14-14M4 0l-10-10M0 4l-10-10"/></g>
      <g id="i-spiral"><path d="M0 0a3 3 0 0 1 6 0a6 6 0 0 1-12 0a9 9 0 0 1 18 0a12 12 0 0 1-24 0"/></g>
    </defs>
    <g transform="translate(0,120)">
      <use href="#i-planet" x="66"/><use href="#i-flag" x="125"/><use href="#i-rocket" x="184"/><use href="#i-ufo" x="243"/><use href="#i-robot" x="302"/><use href="#i-helmet" x="361"/><use href="#i-sun" x="420"/><use href="#i-sat" x="479"/>
    </g>
    <g transform="translate(0,176)">
      <use href="#i-robot" x="66"/><use href="#i-spiral" x="125"/><use href="#i-planet" x="184"/><use href="#i-scope" x="243"/><use href="#i-ufo" x="302"/><use href="#i-ring" x="361"/><use href="#i-comet" x="420"/><use href="#i-sat" x="479"/>
    </g>
    <g transform="translate(0,234)">
      <use href="#i-helmet" x="66"/><use href="#i-ring" x="125"/><use href="#i-scope" x="184"/><use href="#i-rocket" x="243"/><use href="#i-planet" x="302"/><use href="#i-ufo" x="361"/><use href="#i-helmet" x="420"/><use href="#i-comet" x="479"/>
    </g>
  </svg>
</section>

<!-- Contact -->
<section class="slide col-b" style="top:2074px;background:radial-gradient(ellipse at 50% 45%,#2a2658 0%,#16143a 55%,#0c0b22 100%)">
  <div class="abs" style="top:128px;width:553px;text-align:center;font-size:9px;font-weight:600;letter-spacing:1px;color:#8f8bb8">The Meadow Fellowship</div>
  <div class="abs" style="top:164px;width:553px;text-align:center;font-size:23px;font-weight:700">CONTACT US</div>
  <div class="abs" style="top:193px;width:553px;text-align:center;font-size:8px;letter-spacing:1.2px">themeadow.org</div>
</section>

</body>
</html>
```